Website Re-design

Hi, I'm looking for help in redesigning my web site. I currently have a site www.brightmoorlamps.example where I sell lamps, and while I like some aspects of the design, you can tell that I have done the graphics myself and am not a pro at it. I'd like help in redesigning it, and am open to completely new design graphics. I have made the 3 slider images myself, and I feel they could be a bit better, but I am not sure how to do it. For example, on the homepage, the 'About Us', 'Secured Shopping', and '$10 Off' graphics don't go well with the rest of the page. I would like more cohesion in the design and more visual interest in the header, which is pretty basic right now. Also, that the bottom footer is black, I would like instead something else. I am looking for just the layout of the homepage, and possibly once that is done to work on more visual interest in some of the informational pages and product pages. I am looking for just the design in the form of a photoshop file or files that I can incorporate into my site. Thank you!
Updates

Project Deadline Extended
Reason: I just made this project payment committed, so I'd like a chance for designers who only choose payment committed projects to submit artwork. Thank you.

This project is now payment guaranteed/ committed.  Thanks.

Industry/Entity Type

Shopping

```html
<!DOCTYPE html>
<html lang="en">
<head>
<meta charset="utf-8">
<title>Brightmoor Lamps — Home</title>
<link href="https://fonts.googleapis.com/css2?family=Arimo:wght@400;700&family=Great+Vibes&family=Dancing+Script:wght@500&display=swap" rel="stylesheet">
<style>
  :root {
    --teal: #56a9a8;
    --teal-bright: #3fa9b0;
    --teal-dark: #0f5458;
    --teal-soft: #e8f4f4;
    --bar: #3f3f41;
    --ink: #333;
    --footer: #0f4649;
    --footer-deep: #0b3739;
    --footer-base: #082a2c;
    --footer-head: #8fd6d4;
    --footer-link: #bcd9d9;
    --blue: #1b9fe0;
    --blue-deep: #0a7cc6;
  }
  * { box-sizing: border-box; margin: 0; padding: 0; }
  html, body { width: 1200px; height: 1000px; overflow: hidden; }
  body {
    position: relative;
    font-family: "Arimo", Arial, sans-serif;
    color: var(--ink);
    background: repeating-linear-gradient(135deg, #fff 0 3px, #f7f7f7 3px 4px);
  }
  .abs { position: absolute; }

  /* top utility bar */
  .utility-bar { left: 0; top: 0; width: 1200px; height: 30px; background: linear-gradient(#4a4a4c, #363638); }
  .utility-link { position: absolute; top: 10px; font-size: 9px; line-height: 10px; color: #c8c8c8; white-space: nowrap; }
  .utility-link .accent { color: var(--teal-bright); }
  .utility-bar .divider { position: absolute; top: 5px; width: 1px; height: 20px; background: #5d5d5f; }
  .cart-count { color: #f2b632; font-weight: 700; }
  .checkout { position: absolute; left: 888px; top: 0; width: 81px; height: 30px; background: var(--teal); color: #fff; font-size: 8px; font-weight: 700; text-align: center; line-height: 31px; }

  /* header */
  .brand { left: 268px; top: 54px; display: flex; align-items: center; gap: 8px; }
  .brand-mark { width: 34px; height: 34px; border: 2px solid #555; border-radius: 50%; }
  .brand-name { font-size: 18px; line-height: 20px; color: #555; font-weight: 400; }
  .signup { display: flex; height: 28px; }
  .signup .field { width: 122px; border: 1px solid #ddd; background: #fff; font-size: 8px; color: #999; padding-left: 7px; line-height: 26px; white-space: nowrap; overflow: hidden; }
  .signup .go { width: 61px; background: var(--teal); color: #fff; font-size: 9px; font-weight: 700; text-align: center; line-height: 28px; }
  .header-signup { left: 786px; top: 40px; }
  .main-nav { left: 584px; top: 80px; width: 385px; border-top: 1px solid #e6e6e6; height: 34px; }
  .main-nav a { position: absolute; top: 14px; font-size: 9px; font-weight: 700; color: #888; text-decoration: none; letter-spacing: .2px; }
  .main-nav a.active { color: var(--teal-bright); }
  .main-nav .marker { position: absolute; left: 0; top: -1px; width: 37px; height: 2px; background: var(--teal-bright); }

  /* hero */
  .hero-frame { left: 268px; top: 114px; width: 702px; height: 396px; background: #fff; border: 1px solid #e2e2e2; box-shadow: 0 12px 10px -10px rgba(0,0,0,.18); }
  .hero-scene { position: absolute; left: 4px; top: 5px; width: 690px; height: 383px;
    background: linear-gradient(100deg, #2f8a8d 0, #4aa9ab 35%, #7fcfd0 70%, #a7e0e1 100%); }
  .hero-floor { position: absolute; left: 4px; top: 294px; width: 690px; height: 94px;
    background: linear-gradient(#eef2f2 0, #eef2f2 8%, #d5dbdc 9%, #c6cdce 100%); }
  .hero-title { position: absolute; left: 76px; top: 88px; font-family: "Great Vibes", cursive; font-size: 50px; line-height: 64px; color: #fff; text-shadow: 1px 2px 3px rgba(0,0,0,.35); }
  .hero-product { position: absolute; left: 65px; top: 248px; font-size: 14px; color: #111; text-shadow: 0 0 3px rgba(255,255,255,.6); }
  .hero-cta { position: absolute; left: 98px; top: 317px; width: 142px; height: 46px; background: linear-gradient(var(--blue), var(--blue-deep)); border: 1px solid #7cc9ef; color: #fff; font-size: 12px; text-align: center; line-height: 44px; }

  /* feature cards – one shared style */
  .card { top: 560px; width: 222px; height: 176px; }
  .card-panel { position: absolute; left: 14px; top: 0; width: 194px; height: 128px; background: #fff; border: 1px solid #d7e8e8; border-top: 4px solid var(--teal); }
  .card-band { position: absolute; left: 0; top: 128px; width: 222px; height: 47px; background: var(--teal-dark); box-shadow: 0 10px 8px -8px rgba(0,0,0,.25); }
  .card-band .label { display: block; text-align: center; line-height: 47px; font-size: 9px; font-weight: 700; color: #fff; letter-spacing: .3px; }
  .fold { position: absolute; top: 118px; width: 14px; height: 10px; }
  .card-head { position: absolute; top: 20px; left: 0; right: 0; display: flex; align-items: center; justify-content: center; gap: 8px; }
  .card-title { font-family: "Dancing Script", cursive; font-size: 19px; color: var(--teal-dark); }
  .card-icon { width: 30px; height: 30px; flex: none; }
  .card-copy { position: absolute; left: 10px; right: 10px; top: 70px; font-size: 8.5px; font-weight: 700; color: #444; text-align: center; line-height: 12px; }

  /* footer – deep teal instead of black */
  .footer { left: 0; top: 785px; width: 1200px; height: 195px; background: linear-gradient(var(--footer), var(--footer-deep)); }
  .footer-col { position: absolute; top: 43px; }
  .footer-col h3 { font-size: 12px; font-weight: 400; color: var(--footer-head); margin-bottom: 16px; }
  .footer-col li { list-style: none; font-size: 8px; color: var(--footer-link); line-height: 15.2px; white-space: nowrap; }
  .footer-col li.current { color: var(--footer-head); text-decoration: underline; }
  .footer-rule { position: absolute; left: 733px; top: 37px; width: 1px; height: 133px; background: rgba(255,255,255,.12); }
  .social { position: absolute; left: 786px; top: 71px; display: flex; gap: 7px; }
  .social span { width: 22px; height: 22px; border-radius: 50%; }
  .footer-signup { position: absolute; left: 786px; top: 103px; }
  .footer-signup .field { border: none; }
  .legal { left: 0; top: 980px; width: 1200px; height: 20px; background: var(--footer-base); color: #8fb3b3; font-size: 8px; text-align: center; line-height: 21px; }
</style>
</head>
<body>

<div class="abs utility-bar">
  <span class="utility-link" style="left:584px"><span class="accent">Sign In</span> or Create an Account</span>
  <i class="divider" style="left:710px"></i>
  <span class="utility-link" style="left:726px">My Account</span>
  <i class="divider" style="left:788px"></i>
  <span class="utility-link" style="left:803px">Cart ( <b class="cart-count">5</b> Items)
    <svg width="13" height="10" viewBox="0 0 13 10" style="vertical-align:-1px"><path d="M0 1h2l2 6h7l1.5-4.5H3.2" fill="none" stroke="#c8c8c8" stroke-width="1"/><circle cx="5" cy="9" r="1" fill="#c8c8c8"/><circle cx="10" cy="9" r="1" fill="#c8c8c8"/></svg>
  </span>
  <div class="checkout">CHECK OUT</div>
</div>

<header>
  <div class="abs brand">
    <span class="brand-mark"></span>
    <span class="brand-name">brightmoor<br>lamps</span>
  </div>
  <div class="abs signup header-signup">
    <div class="field">Emails for news, sales, offers</div>
    <div class="go">Sign in &gt;&gt;</div>
  </div>
  <nav class="abs main-nav">
    <i class="marker"></i>
    <a class="active" href="#" style="left:7px">HOME</a>
    <a href="#" style="left:76px">SHOP</a>
    <a href="#" style="left:144px">ABOUT US</a>
    <a href="#" style="left:236px">CONTACT US</a>
  </nav>
</header>

<section class="abs hero-frame">
  <div class="hero-scene" role="img" aria-label="Photo of a blue glass table lamp with a white shade standing on a whitewashed wood floor against a teal wall"></div>
  <div class="hero-floor"></div>
  <div class="hero-title">Light Up<br>The Room</div>
  <div class="hero-product">The Lagoon - Medium Table Lamp</div>
  <div class="hero-cta">SHOP ALL LAMP</div>
</section>

<section>
  <div class="abs card" style="left:267px">
    <svg class="fold" style="left:0" viewBox="0 0 14 10"><path d="M14 0V10H0z" fill="#0a3b3e"/></svg>
    <svg class="fold" style="left:208px" viewBox="0 0 14 10"><path d="M0 0V10H14z" fill="#0a3b3e"/></svg>
    <div class="card-panel">
      <div class="card-head">
        <svg class="card-icon" viewBox="0 0 30 30"><circle cx="15" cy="15" r="14" fill="#e8f4f4" stroke="#56a9a8" stroke-width="1.5"/><rect x="10" y="9" width="10" height="12" fill="none" stroke="#0f5458" stroke-width="1.5"/><path d="M12 13h6M12 16h6M12 19h4" stroke="#0f5458" stroke-width="1"/></svg>
        <span class="card-title">About Us</span>
      </div>
      <p class="card-copy">Brightmoor Lamps provides beautiful and artistic home and hospitality lighting.</p>
    </div>
    <div class="card-band"><span class="label">READ MORE &gt;&gt;</span></div>
  </div>

  <div class="abs card" style="left:514px">
    <svg class="fold" style="left:0" viewBox="0 0 14 10"><path d="M14 0V10H0z" fill="#0a3b3e"/></svg>
    <svg class="fold" style="left:208px" viewBox="0 0 14 10"><path d="M0 0V10H14z" fill="#0a3b3e"/></svg>
    <div class="card-panel">
      <div class="card-head">
        <svg class="card-icon" viewBox="0 0 30 30"><circle cx="15" cy="15" r="14" fill="#e8f4f4" stroke="#56a9a8" stroke-width="1.5"/><path d="M9 15.5l4 4 8-9" fill="none" stroke="#0f5458" stroke-width="2.2" stroke-linecap="round" stroke-linejoin="round"/></svg>
        <span class="card-title">Secured Shopping</span>
      </div>
      <p class="card-copy">Shopping at Brightmoor Lamps is secured and protected by industry standard best practices.</p>
    </div>
    <div class="card-band"><span class="label">READ MORE &gt;&gt;</span></div>
  </div>

  <div class="abs card" style="left:750px">
    <svg class="fold" style="left:0" viewBox="0 0 14 10"><path d="M14 0V10H0z" fill="#0a3b3e"/></svg>
    <svg class="fold" style="left:208px" viewBox="0 0 14 10"><path d="M0 0V10H14z" fill="#0a3b3e"/></svg>
    <div class="card-panel">
      <div class="card-head">
        <svg class="card-icon" viewBox="0 0 30 30"><circle cx="15" cy="15" r="14" fill="#e8f4f4" stroke="#56a9a8" stroke-width="1.5"/><path d="M10 20l10-10" stroke="#0f5458" stroke-width="1.8" stroke-linecap="round"/><circle cx="11" cy="11" r="2" fill="none" stroke="#0f5458" stroke-width="1.5"/><circle cx="19" cy="19" r="2" fill="none" stroke="#0f5458" stroke-width="1.5"/></svg>
        <span class="card-title">$10 Off</span>
      </div>
      <p class="card-copy">$10 off any purchase when you sign up for our newsletter.</p>
    </div>
    <div class="card-band"><span class="label">SIGN UP &gt;&gt;</span></div>
  </div>
</section>

<footer class="abs footer">
  <div class="footer-col" style="left:268px">
    <h3>Help + Info</h3>
    <ul><li class="current">Contact Us</li><li>Shipping Info</li><li>Returns</li><li>To The Trade</li><li>Privacy Policy</li><li>Terms of Use</li></ul>
  </div>
  <div class="footer-col" style="left:381px">
    <h3>My Account</h3>
    <ul><li>Sign In</li><li>Order Status</li><li>Order History</li><li>View Cart</li><li>Checkout</li></ul>
  </div>
  <div class="footer-col" style="left:491px">
    <h3>About Us</h3>
    <ul><li>Who We Are</li><li>Testimonials</li></ul>
  </div>
  <div class="footer-col" style="left:585px">
    <h3>Contact Us</h3>
    <ul><li>Contacts</li><li>info@brightmoorlamps.example</li></ul>
  </div>
  <i class="footer-rule"></i>
  <div class="footer-col" style="left:786px">
    <h3>Follow Us</h3>
  </div>
  <div class="social">
    <span style="background:#3b5a9a"></span>
    <span style="background:#2aa3dd"></span>
    <span style="background:#c8232c"></span>
  </div>
  <div class="signup footer-signup">
    <div class="field">Emails for news, sales, offers</div>
    <div class="go">Sign in &gt;&gt;</div>
  </div>
</footer>
<div class="abs legal">© Brightmoor Lamps 2013 | All Rights Reserved</div>

</body>
</html>
```